Photography Business, Business Card

Looking for a unique cutting edge card that takes advantage of the latest printing technologies. Please review this site for all the options they office: https://plumeprints.example. If you can think it they can do it. And if you have an idea and do not know if they can do it, I will check into it.
Updates

Target Market(s)

People and places I took images of and future clients.

Industry/Entity Type

Photography

Contact Information for Business Card

Name, cell & email. Colin Hartley, chartley@kvnphoto.example, 318-742-9061

Colors

Designer to choose only greyscale colors for use in the design.

Requirements
Must have
• 100% cutting edge. Is so great, those I hand it to always show it to someone else. A piece of art.
Nice to have
• Blacks, silvers, greys, some red. Maybe other colors?

```html
<!DOCTYPE html>
<html lang="en">
<head>
<meta charset="utf-8">
<title>Colin Hartley – Business Card</title>
<link href="https://fonts.googleapis.com/css2?family=Montserrat:wght@400;500;600&display=swap" rel="stylesheet">
<style>
  :root {
    --page: #e9e9e9;
    --band-light: #d3d3d3;
    --band-dark: #2d2d2d;
    --text-light: #e6e6e6;
    --text-muted: #c9c9c9;
    --divider: #6a6a6a;
    --icon-bg: #cfcfcf;
    --icon-fg: #2d2d2d;
    --lens-light: #4a4a4a;
    --lens-dark: #151515;
    --portrait-light: #f4f4f4;
    --portrait-warm: #d9c3b4;
  }
  html, body {
    margin: 0;
    padding: 0;
    width: 1200px;
    height: 1200px;
    overflow: hidden;
    background: var(--page);
    font-family: "Montserrat", sans-serif;
  }
  .canvas {
    position: relative;
    width: 1200px;
    height: 1200px;
  }
  .card {
    position: absolute;
    left: 150px;
    width: 900px;
    height: 514px;
    border-radius: 42px;
    overflow: hidden;
    background: var(--band-light);
    box-shadow: 0 10px 30px rgba(0,0,0,0.18);
  }
  .card--front { top: 60px; }
  .card--back { top: 626px; }
  .dark-band {
    position: absolute;
    left: 0;
    right: 0;
    top: 96px;
    height: 324px;
    background: var(--band-dark);
  }

  /* Front */
  .portrait {
    position: absolute;
    left: 128px;
    top: 128px;
    width: 124px;
    height: 124px;
    border-radius: 50%;
    border: 4px solid #f2f2f2;
    background: linear-gradient(180deg, var(--portrait-warm) 0%, var(--portrait-light) 100%);
    box-sizing: border-box;
  }
  .identity {
    position: absolute;
    left: 40px;
    top: 282px;
    width: 300px;
    text-align: center;
  }
  .identity__name {
    margin: 0;
    font-weight: 600;
    font-size: 34px;
    letter-spacing: 0.5px;
    color: var(--text-muted);
    line-height: 1.1;
  }
  .identity__role {
    margin: 2px 0 0;
    font-weight: 400;
    font-size: 20px;
    letter-spacing: 1px;
    color: var(--text-light);
  }
  .divider {
    position: absolute;
    left: 388px;
    top: 136px;
    width: 1px;
    height: 200px;
    background: var(--divider);
  }
  .contact {
    position: absolute;
    left: 430px;
    top: 190px;
    margin: 0;
    padding: 0;
    list-style: none;
  }
  .contact__item {
    display: flex;
    align-items: center;
    gap: 14px;
    height: 44px;
    font-size: 25px;
    color: var(--text-light);
    white-space: nowrap;
  }
  .contact__icon {
    width: 30px;
    height: 30px;
    border-radius: 50%;
    background: var(--icon-bg);
    display: flex;
    align-items: center;
    justify-content: center;
    flex: none;
  }

  /* Back */
  .brand {
    position: absolute;
    left: 90px;
    top: 252px;
    color: #ffffff;
    font-weight: 500;
    text-align: right;
  }
  .brand__name {
    margin: 0;
    font-size: 42px;
    line-height: 1.1;
    white-space: nowrap;
  }
  .brand__tag {
    margin: 6px 0 0;
    font-size: 15px;
    letter-spacing: 5px;
  }
  .lens {
    position: absolute;
    left: 468px;
    top: 44px;
    width: 420px;
    height: 420px;
    border-radius: 50%;
    background: radial-gradient(circle at 50% 50%, var(--lens-light) 0%, var(--lens-dark) 100%);
    box-shadow: 0 12px 28px rgba(0,0,0,0.35);
  }
</style>
</head>
<body>
<main class="canvas">

  <section class="card card--front" aria-label="Business card front">
    <div class="dark-band"></div>
    <div class="portrait" role="img" aria-label="Round portrait photo of the photographer"></div>
    <div class="identity">
      <h1 class="identity__name">COLIN HARTLEY</h1>
      <p class="identity__role">PHOTOGRAPHER</p>
    </div>
    <div class="divider"></div>
    <ul class="contact">
      <li class="contact__item">
        <span class="contact__icon">
          <svg width="18" height="18" viewBox="0 0 24 24" aria-hidden="true">
            <path fill="var(--icon-fg)" d="M6.6 10.8a15.1 15.1 0 0 0 6.6 6.6l2.2-2.2a1 1 0 0 1 1-.25 11.4 11.4 0 0 0 3.6.57 1 1 0 0 1 1 1V20a1 1 0 0 1-1 1A17 17 0 0 1 3 4a1 1 0 0 1 1-1h3.5a1 1 0 0 1 1 1c0 1.25.2 2.45.57 3.57a1 1 0 0 1-.25 1z"/>
          </svg>
        </span>
        318-742-9061
      </li>
      <li class="contact__item">
        <span class="contact__icon">
          <svg width="18" height="18" viewBox="0 0 24 24" aria-hidden="true">
            <rect x="3" y="6" width="18" height="12" rx="1.5" fill="var(--icon-fg)"/>
            <path d="M3.5 6.8 12 13l8.5-6.2" fill="none" stroke="var(--icon-bg)" stroke-width="1.6"/>
          </svg>
        </span>
        chartley@kvnphoto.example
      </li>
    </ul>
  </section>

  <section class="card card--back" aria-label="Business card back">
    <div class="dark-band"></div>
    <div class="brand">
      <p class="brand__name">Colin Hartley</p>
      <p class="brand__tag">PHOTOGRAPHY</p>
    </div>
    <div class="lens" role="img" aria-label="Illustration of a camera zoom lens seen from the front"></div>
  </section>

</main>
</body>
</html>
```